Flyer-Design für Vertrieb von LED-Beleuchtung
Zielgruppe
Vertrieb von Led Beleuchtung,, für Biergärten
Shop-Adresse lautet www.brilo-nox-markt.de diese sollte auch unbedingt mit rein!
Aufgabenstellung
Es geht Hauptsächlich nur um Bunte Led Birnen und die dazugehörigen Fassungen.
Daher bitte eigene Bilder benutzen und zusätzlich noch welche suchen die passen würden.
Aussagen soll es wie sehr man durch die Umstellung auf unsere Birnen sparen kann und dass sie besser Leuchten als normale und nicht kaputt gehen. 2 alte Flyerversuche von mir selbst liegen bei zwecks preise etc. Die Antwortkarte darf nicht mehr drauf sein da dies bereits Formatprobleme mit der Post gab

```html
<!DOCTYPE html>
<html lang="de">
<head>
<meta charset="utf-8">
<title>Brilo-Nox – Flyer LED-Beleuchtung</title>
<link rel="stylesheet" href="https://fonts.googleapis.com/css2?family=Roboto:ital,wght@0,300;0,400;0,700;0,900;1,700&family=Roboto+Condensed:wght@400;700&display=swap">
<style>
  :root {
    --stage: #2f2a35;
    --paper: #f3f3f2;
    --ink: #1a1a1a;
    --ink-soft: #555;
    --accent: #2f6fd6;
    --night-1: #1b1420;
    --night-2: #6a4320;
    --night-3: #2a2f5a;
    --bokeh-1: #13235c;
    --bokeh-2: #d9a646;
    --bar: #f1ece6;
  }
  * { box-sizing: border-box; margin: 0; padding: 0; }
  html, body { width: 1200px; height: 2400px; overflow: hidden; }
  body {
    background: var(--stage);
    font-family: "Roboto", Arial, sans-serif;
    color: var(--ink);
    display: flex; flex-direction: column; align-items: center;
    justify-content: center; gap: 40px;
  }
  .spread { width: 800px; display: flex; flex-direction: column; box-shadow: 0 18px 40px rgba(0,0,0,.45); }
  .panel { position: relative; width: 800px; height: 377px; overflow: hidden; }
  .panel + .panel { border-top: 1px solid rgba(0,0,0,.15); }
  .photo { position: absolute; inset: 0; }

  /* Cover */
  .cover .photo { background:
      radial-gradient(ellipse at 30% 30%, rgba(230,150,60,.55), transparent 55%),
      radial-gradient(ellipse at 80% 75%, rgba(60,80,170,.55), transparent 50%),
      linear-gradient(135deg, var(--night-1), var(--night-2) 45%, var(--night-3)); }
  .headline { position: absolute; left: 120px; top: 70px; display: flex; flex-direction: column; gap: 5px; }
  .headline span { background: var(--bar); color: #111; padding: 2px 16px; width: fit-content; line-height: 1.05; }
  .headline .light { font-weight: 300; font-size: 52px; }
  .headline .heavy { font-weight: 900; font-size: 56px; letter-spacing: -1px; }
  .headline .url { font-weight: 300; font-size: 28px; padding: 4px 16px; }

  /* Contact */
  .contact { background: var(--paper); }
  .contact-text { position: absolute; left: 80px; top: 90px; font-size: 16px; line-height: 1.4; }
  .contact-text .name { font-weight: 700; }
  .contact-text .claim { color: var(--accent); font-weight: 700; margin-top: 22px; text-transform: uppercase; }
  .contact-text .web { font-weight: 700; margin-top: 22px; }
  .bulb { position: absolute; border-radius: 50% 50% 46% 46%; }
  .bulb-blue { right: 120px; top: 90px; width: 190px; height: 170px; background: radial-gradient(circle at 40% 35%, #5e93d8, #2b5fb0 70%); }

  /* Info panel */
  .info .photo { background:
      radial-gradient(circle at 20% 80%, rgba(230,180,90,.7), transparent 25%),
      radial-gradient(circle at 65% 85%, rgba(230,180,90,.6), transparent 22%),
      linear-gradient(180deg, var(--bokeh-1), #2a3f86 60%, #473d4c); }
  .info-box { position: absolute; left: 60px; top: 40px; width: 520px; background: rgba(245,245,245,.85); padding: 20px 24px; font-size: 13px; line-height: 1.5; }
  .info-box h2 { display: inline-block; font-size: 20px; font-weight: 900; border: 2px solid var(--ink); padding: 2px 8px; background: #fff; margin-bottom: 10px; }
  .info-box h3 { font-size: 15px; font-weight: 700; margin-bottom: 8px; }
  .info-box p + p { margin-top: 8px; }

  /* Savings */
  .savings { background: var(--paper); padding: 40px 60px; }
  .savings h2 { font-family: "Roboto Condensed", Arial, sans-serif; font-weight: 700; font-size: 26px; text-transform: uppercase; line-height: 1.15; }
  .columns { display: flex; gap: 30px; margin-top: 24px; width: 470px; }
  .columns div { flex: 1; font-size: 12px; line-height: 1.45; color: var(--ink-soft); }
  .columns h4 { font-family: "Roboto Condensed", Arial, sans-serif; color: var(--ink); font-size: 12px; text-transform: uppercase; margin-bottom: 6px; }
  .columns strong { color: var(--ink); display: block; margin-top: 8px; }
  .glow-photo { position: absolute; right: 50px; top: 150px; width: 210px; height: 180px; background: radial-gradient(circle at 50% 45%, #fff6c8, #e8c64a 35%, #8a6a17 80%); }

  /* Exchange */
  .exchange .photo { background:
      radial-gradient(circle at 15% 30%, rgba(240,190,60,.8), transparent 18%),
      radial-gradient(circle at 85% 70%, rgba(60,110,230,.8), transparent 20%),
      radial-gradient(circle at 70% 20%, rgba(240,190,60,.6), transparent 15%),
      linear-gradient(120deg, #1c2a6e, #0f1330 50%, #2a3f9a); }
  .exchange-box { position: absolute; left: 60px; top: 40px; width: 680px; height: 297px; background: var(--paper); padding: 26px 30px; }
  .exchange-box h2 { font-size: 22px; font-weight: 700; font-style: italic; }
  .exchange-box h3 { font-size: 15px; font-weight: 700; margin: 6px 0 12px; width: 360px; }
  .exchange-box p { font-size: 13px; line-height: 1.5; color: var(--ink-soft); width: 360px; }
  .bulb-cluster { position: absolute; right: 30px; top: 60px; width: 230px; height: 180px; border-radius: 40%; background: radial-gradient(circle at 30% 40%, #2f5fd0 0 18%, transparent 19%), radial-gradient(circle at 60% 35%, #2b9a47 0 16%, transparent 17%), radial-gradient(circle at 45% 70%, #d92a2a 0 16%, transparent 17%), radial-gradient(circle at 75% 65%, #f0d12d 0 16%, transparent 17%); }

  /* Offer */
  .offer { background: var(--paper); }
  .bulb-yellow { left: 80px; top: 60px; width: 150px; height: 130px; background: radial-gradient(circle at 40% 35%, #fff36a, #e6cf12 70%); }
  .specs { position: absolute; left: 80px; top: 215px; font-size: 12px; line-height: 1.45; color: var(--ink-soft); }
  .specs b { color: var(--ink); }
  .offer-text { position: absolute; left: 400px; top: 80px; }
  .offer-text h2 { font-family: "Roboto Condensed", Arial, sans-serif; font-size: 24px; font-weight: 700; text-transform: uppercase; line-height: 1.15; }
  .offer-text .lead { font-size: 15px; font-weight: 700; margin-top: 20px; }
  .offer-text .price { font-size: 34px; font-weight: 700; font-style: italic; color: var(--accent); margin-top: 6px; }
  .offer-text .note { font-size: 12px; color: var(--ink-soft); margin-top: 4px; }
</style>
</head>
<body>

<section class="spread outside">
  <div class="panel cover">
    <div class="photo" role="img" aria-label="Nachtaufnahme eines beleuchteten Biergartens mit Lichterketten"></div>
    <h1 class="headline">
      <span class="light">mit uns</span>
      <span class="heavy">geht Ihnen</span>
      <span class="heavy">ein Licht auf</span>
      <span class="url">www.brilo-nox-markt.de</span>
    </h1>
  </div>

  <div class="panel contact">
    <div class="contact-text">
      <p class="name">Brilo-Nox | Jelu Pandor</p>
      <p>Lindenhofweg 7</p>
      <p>71234 Musterstadt</p>
      <p>Deutschland</p>
      <p class="claim">Ihr Partner in Sachen<br>LED-Beleuchtung</p>
      <p class="web">http://www.brilo-nox-markt.de</p>
    </div>
    <div class="bulb bulb-blue" role="img" aria-label="Blaue LED-Birne mit E27-Sockel"></div>
  </div>

  <div class="panel info">
    <div class="photo" role="img" aria-label="Lichterkette vor blauem Abendhimmel mit Unschärfe"></div>
    <div class="info-box">
      <h2>Stromsparende LED-Beleuchtung</h2>
      <h3>Sparen Sie da, wo es Sinn macht – bei Ihren Stromkosten</h3>
      <p>Mit farbigen LED-Birnen setzen Sie Ihren Biergarten stimmungsvoll in Szene und senken gleichzeitig den Stromverbrauch deutlich. Unsere Leuchtmittel strahlen heller als herkömmliche Glühbirnen, bleiben dabei angenehm kühl und halten viele Jahre. Kein ständiges Auswechseln, keine Scherben, keine bösen Überraschungen bei der Abrechnung.</p>
      <p>Rechnen Sie selbst: Schon wenige Lampen machen sich nach einer Saison bezahlt.</p>
    </div>
  </div>
</section>

<section class="spread inside">
  <div class="panel savings">
    <h2>Sparen Sie noch heute Geld –<br>und senken Sie Ihre Stromkosten</h2>
    <div class="columns">
      <div>
        <h4>Holen Sie sich Ihr persönliches Angebot …</h4>
        Gerne beraten wir Sie vor Ort und erstellen Ihnen ein Angebot. Schreiben Sie uns eine E-Mail an
        <strong>info@brilo-nox.de</strong>
      </div>
      <div>
        <h4>… oder bestellen Sie gleich online</h4>
        Wissen Sie bereits, was Sie brauchen? Dann bestellen Sie bequem in unserem Shop unter
        <strong>www.brilo-nox.de</strong>
      </div>
      <div>
        <h4>… und sparen Sie bares Geld!</h4>
        Stellen Sie jetzt um: Bei 100 Birnen mit je 40 Watt weniger Verbrauch sparen Sie jährlich
        <strong>bis zu 4.000 EUR</strong>
        abzüglich Anschaffung bleiben
        <strong>3.898 EUR gespart.</strong>
      </div>
    </div>
    <div class="glow-photo" role="img" aria-label="Leuchtende gelbe LED-Birne in Fassung"></div>
  </div>

  <div class="panel exchange">
    <div class="photo" role="img" aria-label="Bunte Lichtpunkte in Gelb und Blau, unscharf"></div>
    <div class="exchange-box">
      <h2>Einfaches Austauschen …</h2>
      <h3>… und endlose Kombinationsmöglichkeiten dank Standard-Fassungen</h3>
      <p>Unsere LED-Birnen passen in jede handelsübliche E27-Fassung. Einfach alte Birne heraus, neue hinein – fertig. Kombinieren Sie die Farben ganz nach Lust und Anlass und verwandeln Sie Ihren Biergarten in wenigen Minuten.</p>
      <div class="bulb-cluster" role="img" aria-label="Mehrere farbige LED-Birnen in Blau, Grün, Rot, Gelb und Weiß"></div>
    </div>
  </div>

  <div class="panel offer">
    <div class="bulb bulb-yellow" role="img" aria-label="Gelbe LED-Birne mit E27-Sockel"></div>
    <div class="specs">
      <b>Led-Birne Farbig | Fassung E27</b><br>
      IP45 Spritzwasserschutz | Verbrauch 1 Watt<br>
      ca. 40 Lumen | Lebensdauer mind. 30.000 Std
    </div>
    <div class="offer-text">
      <h2>Wir lassen Sie<br>nicht im Dunkeln stehen</h2>
      <p class="lead">Und das zum Sonderpreis.</p>
      <p class="price">nur EUR 2,27 zzgl. Mwst.</p>
      <p class="note">(statt EUR 2,78 – Achtung zeitlich begrenztes Angebot)</p>
    </div>
  </div>
</section>

</body>
</html>
```